Korbin Ventilation's. "We're Dalton beyond the pack"!

Good day< Does your company do face mask? that is question 1. and lets finish the stationary design and I will pay for that now? 2 If your company has BLACK HATS now I would want to do some of those? 3 I notice do you do BANNER'S and or something I can put on van's magnet type or on a building! )k that's enough but for now lets start with the stationary stuff? let me know you should have my information, and the design look's GREAT!!! Thank you..

```html
<!DOCTYPE html>
<html lang="en">
<head>
<meta charset="utf-8">
<title>Korbin Ventilation's — Letterhead</title>
<link href="https://fonts.googleapis.com/css2?family=Open+Sans:wght@400;700&family=Roboto:wght@400&display=swap" rel="stylesheet">
<style>
  :root {
    --backdrop: #dcdcdc;
    --paper: #f7f7f7;
    --ink: #0a0a0a;
    --body-text: #8c8c8c;
    --contact-text: #555555;
    --accent-green: #9db05a;
    --white: #ffffff;
  }
  * { margin: 0; padding: 0; box-sizing: border-box; }
  html, body {
    width: 1153px;
    height: 1200px;
    overflow: hidden;
    background: var(--backdrop);
  }
  .letterhead {
    position: absolute;
    left: 146px;
    top: 0;
    width: 860px;
    height: 1200px;
    background: var(--paper);
    font-family: "Open Sans", Arial, sans-serif;
    overflow: hidden;
  }
  .brand {
    position: absolute;
    left: 77px;
    top: 90px;
    width: 170px;
    text-align: center;
  }
  .brand-mark {
    display: block;
    width: 46px;
    height: 46px;
    margin: 0 auto 8px;
    border-radius: 50%;
    background: var(--ink);
  }
  .brand-name {
    font-weight: 700;
    font-size: 19px;
    line-height: 22px;
    color: var(--ink);
  }
  .brand-tagline {
    margin-top: 4px;
    font-weight: 700;
    font-size: 11px;
    color: var(--ink);
  }
  .contact {
    position: absolute;
    left: 602px;
    top: 94px;
    width: 200px;
    font-family: "Roboto", Arial, sans-serif;
    font-size: 15px;
    color: var(--contact-text);
  }
  .contact-address { line-height: 19px; margin-bottom: 6px; }
  .contact-line {
    display: flex;
    align-items: center;
    gap: 5px;
    height: 20px;
  }
  .contact-icon { width: 14px; height: 14px; flex: none; }
  .letter-body {
    position: absolute;
    left: 77px;
    top: 314px;
    width: 704px;
    font-size: 16px;
    line-height: 23px;
    color: var(--body-text);
  }
  .letter-body p { margin-bottom: 23px; text-align: justify; }
  .footer-wave {
    position: absolute;
    left: 0;
    bottom: 0;
    width: 860px;
    height: 93px;
  }
</style>
</head>
<body>
  <main class="letterhead">
    <header>
      <div class="brand">
        <span class="brand-mark"></span>
        <div class="brand-name">Korbin Ventilation's</div>
        <div class="brand-tagline">"We're Dalton beyond the pack"</div>
      </div>
      <address class="contact" style="font-style: normal;">
        <div class="contact-address">Harlow Court, 12 Mercer Lane,<br>London, SE4 2QT</div>
        <div class="contact-line">
          <svg class="contact-icon" viewBox="0 0 14 14" aria-hidden="true">
            <path d="M1 5 C1 2 13 2 13 5 L10 6 L9 4 L5 4 L4 6 Z" fill="var(--accent-green)"/>
            <rect x="3" y="7" width="8" height="5" rx="1" fill="var(--accent-green)"/>
          </svg>
          <span>555.208.4417</span>
        </div>
        <div class="contact-line">
          <svg class="contact-icon" viewBox="0 0 14 14" aria-hidden="true">
            <rect x="1" y="3" width="12" height="8" fill="var(--accent-green)"/>
            <path d="M1 3 L7 8 L13 3" stroke="var(--white)" stroke-width="1.2" fill="none"/>
          </svg>
          <span>info@korbinvent.com</span>
        </div>
        <div class="contact-line">
          <svg class="contact-icon" viewBox="0 0 14 14" aria-hidden="true">
            <circle cx="7" cy="7" r="6" fill="var(--accent-green)"/>
            <path d="M4 4 C6 5 5 7 7 8 C8 9 6 11 7 12 M9 2 C10 4 12 5 12 7" stroke="var(--white)" stroke-width="1.2" fill="none"/>
          </svg>
          <span>www.korbinvent.com</span>
        </div>
      </address>
    </header>

    <section class="letter-body">
      <p>Dear customer,</p>
      <p>Lorem ipsum dolor sit amet, consectetur adipisicing elit, sed do eiusmod tempor incididunt ut labore et dolore magna aliqua. Ut enim ad minim veniam, quis nostrud exercitation ullamco laboris nisi ut aliquip ex ea commodo consequat. Duis aute irure dolor in reprehenderit in voluptate velit esse cillum dolore eu fugiat nulla pariatur. Excepteur sint occaecat cupidatat non proident, sunt in culpa qui officia deserunt mollit anim id est laborum.</p>
      <p>Lorem ipsum dolor sit amet, consectetur adipisicing elit, sed do eiusmod tempor incididunt ut labore et dolore magna aliqua. Ut enim ad minim veniam, quis nostrud exercitation ullamco laboris nisi ut aliquip ex ea commodo consequat. Duis aute irure dolor in reprehenderit in voluptate velit esse cillum dolore eu fugiat nulla pariatur. Excepteur sint occaecat cupidatat non proident, sunt in culpa qui officia deserunt mollit anim id est laborum.</p>
      <p>Lorem ipsum dolor sit amet, consectetur adipisicing elit, sed do eiusmod tempor incididunt ut labore et dolore magna aliqua. Ut enim ad minim veniam, quis nostrud exercitation ullamco laboris nisi ut aliquip ex ea commodo consequat. Duis aute irure dolor in reprehenderit in voluptate velit esse cillum dolore eu fugiat nulla pariatur. Excepteur sint occaecat cupidatat non proident, sunt in culpa qui officia deserunt mollit anim id est laborum.</p>
      <p>Lorem ipsum dolor sit amet, consectetur adipisicing elit, sed do eiusmod tempor incididunt ut labore et dolore magna aliqua. Ut enim ad minim veniam, quis nostrud exercitation ullamco laboris nisi ut aliquip ex ea commodo consequat. Duis aute irure dolor in reprehenderit.</p>
      <p>Yours Sincerely,</p>
    </section>

    <svg class="footer-wave" viewBox="0 0 1008 108" preserveAspectRatio="none" aria-hidden="true">
      <path d="M0 40 C160 85 400 92 612 28 C420 72 200 82 0 58 Z" fill="var(--accent-green)"/>
      <path d="M0 72 C220 112 470 96 1008 38 L1008 108 L0 108 Z" fill="var(--ink)"/>
      <path d="M445 77 C650 30 850 0 1008 18 L1008 28 C820 12 650 42 445 77 Z" fill="var(--ink)"/>
    </svg>
  </main>
</body>
</html>
```